Stonebrook Glazeworks Inc. Business Card

Looking for business card with embossed raised logo print. Logo provided and want it to be most prominent image on card. Color pallet of black, red, white or charcoal gray preferred for brand recognition. Simple contact information on front and list description of services provided on back. Services included....Custom Showers, Tub Surrounds, Backsplashes, Fireplaces, Floors and more. Dustless Demolition, Lifetime Warranty, Proud member of the Federated Surface Installers Guild

Target Market(s)

High end residential remodel work and new home builders

Contact Information for Business Card

Phone # (402) 555-0193 email address, Stonebrookgw@mailvane.net Dorian Kovalski Owner

Requirements
Must have
• Business logo as most prominent image on the front of business card. Along with contact information and name Dorian Kovalski. Would like to see services provided on the back of the card.

```html
<!DOCTYPE html>
<html lang="en">
<head>
<meta charset="utf-8">
<title>Stonebrook Glazeworks Inc. – Business Card</title>
<link href="https://fonts.googleapis.com/css2?family=Open+Sans:wght@300;400;600&display=swap" rel="stylesheet">
<style>
  :root {
    --page: #f2f2f2;
    --card-black: #050505;
    --brand-red: #e3232b;
    --signal-red: #f01207;
    --deep-red: #5a0a08;
    --ink-white: #ffffff;
  }
  * { margin: 0; padding: 0; box-sizing: border-box; }
  html, body {
    width: 672px; height: 1200px; overflow: hidden;
    background: var(--page);
    font-family: "Open Sans", Arial, sans-serif;
  }
  .sheet {
    position: relative; width: 672px; height: 1200px;
    display: flex; flex-direction: column; align-items: center; justify-content: center; gap: 6px;
  }
  .card {
    position: relative; width: 632px; height: 360px;
    background: var(--card-black); overflow: hidden;
  }
  .card-art { position: absolute; inset: 0; width: 100%; height: 100%; }

  /* front */
  .brand { position: absolute; left: 26px; top: 26px; display: flex; align-items: flex-start; gap: 12px; }
  .brand-square { width: 52px; height: 52px; background: var(--brand-red); margin-top: 4px; }
  .brand-name { color: var(--brand-red); font-weight: 600; line-height: 1; }
  .brand-name .line-main { display: block; font-size: 40px; letter-spacing: 1px; }
  .brand-name .line-sub { display: block; font-size: 17px; letter-spacing: 5px; margin-top: 6px; }

  .contact { position: absolute; right: 16px; top: 248px; text-align: right; color: var(--ink-white); }
  .contact-name { font-size: 25px; font-weight: 300; letter-spacing: 0.5px; margin-bottom: 8px; }
  .contact-line { display: flex; justify-content: flex-end; align-items: center; gap: 8px; font-size: 17px; font-weight: 400; height: 27px; }
  .contact-icon { width: 23px; height: 23px; border-radius: 50%; background: var(--signal-red); display: flex; align-items: center; justify-content: center; flex: none; }
  .contact-icon svg { width: 13px; height: 13px; }

  /* back */
  .services { position: absolute; left: 382px; top: 90px; color: var(--ink-white); }
  .services-title { font-size: 21px; font-weight: 400; margin-left: 23px; margin-bottom: 8px; }
  .services-list { list-style: none; }
  .services-list li { font-size: 16.5px; line-height: 24px; display: flex; align-items: center; gap: 11px; }
  .bullet { width: 12px; height: 12px; border-radius: 50%; background: var(--signal-red); flex: none; }
  .membership { position: absolute; left: 78px; top: 323px; color: var(--ink-white); font-size: 17px; display: flex; align-items: center; gap: 12px; white-space: nowrap; }
</style>
</head>
<body>
<main class="sheet">

  <section class="card card-front" aria-label="Business card front">
    <svg class="card-art" viewBox="0 0 632 360" aria-hidden="true">
      <defs>
        <radialGradient id="frontGlow" cx="1" cy="1" r="0.9">
          <stop offset="0" stop-color="#6a0a06"/>
          <stop offset="1" stop-color="#050505" stop-opacity="0"/>
        </radialGradient>
        <linearGradient id="frontSweep" x1="0" y1="0" x2="1" y2="0">
          <stop offset="0" stop-color="#050505" stop-opacity="0"/>
          <stop offset="0.5" stop-color="#d0100a"/>
          <stop offset="1" stop-color="#f01207"/>
        </linearGradient>
      </defs>
      <rect x="0" y="0" width="632" height="360" fill="url(#frontGlow)"/>
      <path d="M120 360 Q380 300 632 200 L632 236 Q400 320 200 360 Z" fill="url(#frontSweep)" opacity="0.85"/>
      <rect x="26" y="112" width="180" height="2" fill="var(--brand-red)"/>
    </svg>

    <div class="brand">
      <span class="brand-square"></span>
      <span class="brand-name">
        <span class="line-main">STONEBROOK</span>
        <span class="line-sub">GLAZEWORKS INC.</span>
      </span>
    </div>

    <div class="contact">
      <p class="contact-name">DORIAN KOVALSKI</p>
      <p class="contact-line">(402) 555-0193
        <span class="contact-icon"><svg viewBox="0 0 16 16"><path d="M4 1.5 6.2 4.6 4.9 6.2c.9 2 2.5 3.7 4.6 4.7l1.5-1.3 3 2.3-1.3 2.3C8 14.3 1.8 8.1 1.8 3.2Z" fill="#fff"/></svg></span>
      </p>
      <p class="contact-line">Stonebrookgw@mailvane.net
        <span class="contact-icon"><svg viewBox="0 0 16 16"><rect x="1.5" y="3.5" width="13" height="9" fill="#fff"/><path d="M1.5 3.5 8 9l6.5-5.5M1.5 12.5 6 8m8.5 4.5L10 8" stroke="#f01207" stroke-width="1.2" fill="none"/></svg></span>
      </p>
    </div>
  </section>

  <section class="card card-back" aria-label="Business card back">
    <svg class="card-art" viewBox="0 0 632 360" aria-hidden="true">
      <defs>
        <radialGradient id="backGlow" cx="0" cy="0.55" r="0.75">
          <stop offset="0" stop-color="#8a0d07"/>
          <stop offset="1" stop-color="#050505" stop-opacity="0"/>
        </radialGradient>
      </defs>
      <rect x="0" y="0" width="632" height="360" fill="url(#backGlow)"/>
      <rect x="382" y="70" width="2" height="220" fill="var(--brand-red)" opacity="0.6"/>
    </svg>

    <div class="services">
      <h2 class="services-title">SERVICES</h2>
      <ul class="services-list">
        <li><span class="bullet"></span>Custom Showers,</li>
        <li><span class="bullet"></span>Tub Surrounds,</li>
        <li><span class="bullet"></span>Backsplashes,</li>
        <li><span class="bullet"></span>Fireplaces,</li>
        <li><span class="bullet"></span>Floors and more.</li>
        <li><span class="bullet"></span>Dustless Demolition,</li>
        <li><span class="bullet"></span>Lifetime Warranty,</li>
      </ul>
    </div>

    <p class="membership"><span class="bullet"></span>Proud member of the Federated Surface Installers Guild</p>
  </section>

</main>
</body>
</html>
```